Copperleaf Motorized Shade Business Card

Hello, we've had our logo made. Now we are looking for a clean and cool looking business card. One side can just be the logo with any design elements that might look good with it. The other side will be Name, Phone Number and Email. There will not be an address on the card.

```html
<!DOCTYPE html>
<html lang="en">
<head>
<meta charset="utf-8">
<title>Copperleaf Motorized Shade Business Card</title>
<link href="https://fonts.googleapis.com/css2?family=Roboto:wght@400;500&display=swap" rel="stylesheet">
<style>
  :root {
    --page-bg: #e6e6e4;
    --card-bg: #2c2c2c;
    --edge-blue: #12a6e6;
    --accent-blue: #1aa8e8;
    --text-light: #e6e6e6;
    --rule: #cfcfcf;
    --brand-white: #ffffff;
    --brand-grey: #4a4a4a;
  }
  * { box-sizing: border-box; margin: 0; padding: 0; }
  html, body { width: 1200px; height: 801px; overflow: hidden; }
  body {
    background: var(--page-bg);
    font-family: "Roboto", Arial, sans-serif;
    position: relative;
  }
  .card {
    position: absolute;
    width: 540px;
    height: 310px;
    background: var(--card-bg);
    border-bottom: 4px solid var(--edge-blue);
    border-left: 2px solid var(--edge-blue);
    box-shadow: 0 10px 24px rgba(0,0,0,0.25);
  }
  .card-front { left: 40px; top: 245px; }
  .card-back { left: 620px; top: 245px; }

  .brand {
    position: absolute;
    display: flex;
    align-items: center;
    gap: 10px;
    font-family: "Roboto", Arial, sans-serif;
    font-weight: 500;
    line-height: 1.1;
    text-transform: uppercase;
    white-space: nowrap;
  }
  .brand-mark { flex: none; }
  .card-front .brand {
    top: 48px; right: 36px;
    font-size: 22px;
    color: var(--brand-white);
  }
  .card-front .brand-mark { width: 16px; height: 16px; background: var(--accent-blue); }

  .divider {
    position: absolute;
    left: 36px; right: 36px; top: 186px;
    height: 1px;
    background: var(--rule);
  }
  .person { position: absolute; left: 36px; top: 132px; }
  .person-name { color: var(--accent-blue); font-size: 22px; font-weight: 500; }
  .person-role { color: var(--text-light); font-size: 15px; margin-top: 2px; }

  .contacts {
    position: absolute; left: 36px; top: 202px;
    list-style: none;
    color: var(--text-light);
    font-size: 15px;
  }
  .contacts li { display: flex; align-items: center; gap: 10px; height: 24px; }
  .contacts svg { width: 13px; height: 13px; flex: none; }

  .card-back .brand {
    left: 50%; top: 50%;
    transform: translate(-50%, -50%);
    font-size: 34px;
    color: var(--brand-grey);
  }
  .card-back .brand-mark { width: 26px; height: 26px; background: var(--brand-grey); }
</style>
</head>
<body>
  <section class="card card-front" aria-label="Business card front">
    <div class="brand"><span class="brand-mark"></span><span>Copperleaf<br>Motorized Shade</span></div>
    <div class="person">
      <p class="person-name">Daniel Reyes</p>
      <p class="person-role">Manager</p>
    </div>
    <div class="divider"></div>
    <ul class="contacts">
      <li><svg viewBox="0 0 16 16" aria-hidden="true"><path d="M4 1l3 3-2 2c1 2 3 4 5 5l2-2 3 3-2 2C7 14 2 9 2 3z" fill="var(--accent-blue)"/></svg>555-014-2270</li>
      <li><svg viewBox="0 0 16 16" aria-hidden="true"><rect x="1.5" y="3.5" width="13" height="9" fill="none" stroke="var(--accent-blue)" stroke-width="1.5"/><path d="M1.5 3.5l6.5 5 6.5-5" fill="none" stroke="var(--accent-blue)" stroke-width="1.5"/></svg>hello@copperleafshades.com</li>
      <li><svg viewBox="0 0 16 16" aria-hidden="true"><circle cx="8" cy="8" r="6.5" fill="none" stroke="var(--accent-blue)" stroke-width="1.5"/><path d="M1.5 8h13M8 1.5c-3 3.5-3 9.5 0 13M8 1.5c3 3.5 3 9.5 0 13" fill="none" stroke="var(--accent-blue)" stroke-width="1.2"/></svg>www.copperleafshades.com</li>
    </ul>
  </section>

  <section class="card card-back" aria-label="Business card back">
    <div class="brand"><span class="brand-mark"></span><span>Copperleaf<br>Motorized Shade</span></div>
  </section>
</body>
</html>
```